Design our letter, business card, powerpoint and more

We have a logo and want a design for our business use. Letters (word template), business card (for printing) powerpoint presentation (template) and more.

```html
<!DOCTYPE html>
<html lang="en">
<head>
<meta charset="utf-8">
<title>Presentation Template Slides</title>
<link href="https://fonts.googleapis.com/css2?family=Maven+Pro:wght@400;500;600;700&family=Lato:wght@400&display=swap" rel="stylesheet">
<style>
:root{
  --stage-inner:#3a3a3a;
  --stage-outer:#141414;
  --card:#ffffff;
  --tint:#ebf3fd;
  --tint-soft:#f3f8fe;
  --ink:#2d3338;
  --body:#6c7680;
  --accent:#4fa6e8;
  --accent-soft:#a9d2f3;
  --track:#d9dee4;
  --brand:#6f8294;
  --ring:#2e3639;
}
*{margin:0;padding:0;box-sizing:border-box}
html,body{width:1200px;height:675px;overflow:hidden}
body{
  background:radial-gradient(ellipse at 50% 50%,var(--stage-inner) 0%,#262626 55%,var(--stage-outer) 100%);
  position:relative;font-family:'Maven Pro',sans-serif;color:var(--ink);
}
.slide{position:absolute;width:360px;height:202px;background:var(--card);border-radius:25px;overflow:hidden}
.slide--tint{background:var(--tint)}
.abs{position:absolute}
.brand{display:flex;align-items:center;gap:4px;font-family:'Maven Pro',sans-serif;font-weight:600;color:var(--brand);letter-spacing:.2px}
.brand__dot{width:9px;height:9px;border-radius:50%;background:var(--accent)}
.deck-title{font-weight:700;color:var(--ink);text-align:center}
.subtitle{font-family:'Lato',sans-serif;font-size:3.5px;color:var(--body);text-align:center}
.copy{font-family:'Lato',sans-serif;font-size:4.4px;line-height:1.6;color:var(--body)}
.heading{font-weight:500;color:var(--ink)}
.num{font-size:14px;font-weight:500;color:var(--ink)}
.num-halo{width:44px;height:44px;border-radius:50%;background:#ffffff;opacity:.6}
.skill-label{font-family:'Lato',sans-serif;font-size:3.6px;color:var(--body);display:flex;justify-content:space-between;width:127px}
.track{width:127px;height:6px;background:var(--track);border-radius:1px}
.fill{height:6px;background:var(--accent);border-radius:1px}
.graphic-area{border-radius:8px;background:linear-gradient(135deg,var(--accent-soft) 0%,var(--tint) 100%)}
.stat{background:#eef4fb;border-radius:3px;text-align:center}
.stat__value{font-size:8.5px;font-weight:500;color:var(--ink);line-height:1;padding-top:5px}
.stat__label{font-family:'Lato',sans-serif;font-size:2.8px;color:var(--body);margin-top:3px}
</style>
</head>
<body>

<!-- Cover, plain -->
<section class="slide" style="left:36px;top:103px">
  <div class="brand abs" style="left:0;width:360px;top:82px;justify-content:center;font-size:10px"><span class="brand__dot"></span>NORVIKA</div>
  <h1 class="deck-title abs" style="left:0;width:360px;top:125px;font-size:19px">Presentation</h1>
  <p class="subtitle abs" style="left:0;width:360px;top:151px">Subtitle with some text</p>
</section>

<!-- Cover with photo -->
<section class="slide" style="left:419px;top:103px">
  <svg class="abs" style="left:0;top:0" width="360" height="202">
    <defs>
      <linearGradient id="photoTone" x1="0" y1="0" x2="1" y2="1">
        <stop offset="0" stop-color="#c8a07c"/>
        <stop offset=".45" stop-color="#a57a5c"/>
        <stop offset="1" stop-color="#3e4750"/>
      </linearGradient>
    </defs>
    <g role="img" aria-label="Photo of team members joining fists in a circle">
      <rect x="123" y="19" width="237" height="163" fill="url(#photoTone)"/>
      <circle cx="123" cy="101" r="81" fill="var(--ring)"/>
    </g>
    <circle cx="123" cy="101" r="69" fill="#ffffff"/>
  </svg>
  <div class="brand abs" style="left:54px;width:138px;top:81px;justify-content:center;font-size:8px"><span class="brand__dot" style="width:7px;height:7px"></span>NORVIKA</div>
  <h1 class="deck-title abs" style="left:54px;width:138px;top:110px;font-size:15px">Presentation</h1>
  <p class="subtitle abs" style="left:54px;width:138px;top:134px;font-size:3px">Subtitle with some text</p>
</section>

<!-- Numbered list -->
<section class="slide slide--tint" style="left:801px;top:103px">
  <h2 class="heading abs" style="left:0;width:360px;text-align:center;top:31px;font-size:14px">Numbered List</h2>
  <svg class="abs" style="left:165px;top:55px" width="30" height="10" aria-hidden="true">
    <line x1="4" y1="5" x2="26" y2="5" stroke="var(--accent)" stroke-width="1"/>
    <circle cx="3" cy="5" r="2" fill="var(--accent)"/>
    <circle cx="14" cy="5" r="4.5" fill="var(--accent)"/>
    <circle cx="25" cy="5" r="2" fill="var(--accent)"/>
  </svg>

  <div class="num-halo abs" style="left:38px;top:75px"></div>
  <div class="num abs" style="left:36px;top:68px">01</div>
  <p class="copy abs" style="left:53px;top:80px;width:122px">Lorem ipsum dolor sit amet, consectetur adipiscing elit, sed do eiusmod tempor incididunt ut labore et quis nostrud exercitation ullamco laboris nisi ut</p>

  <div class="num-halo abs" style="left:194px;top:75px"></div>
  <div class="num abs" style="left:192px;top:68px">03</div>
  <p class="copy abs" style="left:208px;top:80px;width:122px">Lorem ipsum dolor sit amet, consectetur adipiscing elit, sed do eiusmod tempor incididunt ut labore et quis nostrud exercitation ullamco laboris nisi ut</p>

  <div class="num-halo abs" style="left:38px;top:135px"></div>
  <div class="num abs" style="left:36px;top:128px">02</div>
  <p class="copy abs" style="left:53px;top:140px;width:122px">Lorem ipsum dolor sit amet, consectetur adipiscing elit, sed do eiusmod tempor incididunt ut labore et quis nostrud exercitation ullamco laboris nisi ut</p>

  <div class="num-halo abs" style="left:194px;top:135px"></div>
  <div class="num abs" style="left:192px;top:128px">04</div>
  <p class="copy abs" style="left:208px;top:140px;width:122px">Lorem ipsum dolor sit amet, consectetur adipiscing elit, sed do eiusmod tempor incididunt ut labore et quis nostrud exercitation ullamco laboris nisi ut</p>
</section>

<!-- Title with progress bars -->
<section class="slide" style="left:36px;top:349px">
  <svg class="abs" style="left:0;top:0" width="360" height="202" aria-hidden="true">
    <circle cx="92" cy="139" r="140" fill="var(--tint)"/>
    <circle cx="92" cy="139" r="72" fill="var(--tint-soft)"/>
    <circle cx="92" cy="139" r="36" fill="var(--tint)"/>
  </svg>
  <h2 class="heading abs" style="left:36px;top:35px;font-size:23px;line-height:29.5px;width:112px">Title text slide with progress bar</h2>
  <svg class="abs" style="left:83px;top:132px" width="16" height="16" aria-hidden="true">
    <circle cx="8" cy="8" r="7.5" fill="var(--accent)"/>
    <path d="M5 8h6M8.5 5.5 11 8l-2.5 2.5" stroke="#fff" stroke-width="1" fill="none"/>
  </svg>
  <p class="copy abs" style="left:191px;top:39px;width:132px">Lorem ipsum dolor sit amet, consectetur adipiscing elit, sed do eiusmod tempor incididunt ut labore et dolore magna aliqua. Ut enim ad minim veniam, quis nostrud exercitation ullamco laboris nisi ut aliquip ullamco ex ea commodo consequat. Duis aute irure dolor ullamco in reprehenderit in voluptate velit esse cillum dolore eu fugiat nulla pariatur. Excepteur sint occaecat cupidatat non proident, sunt in culpa qui officia deserunt mollit anim id est in voluptate velit esse cillum eu laborum.</p>
  <div class="skill-label abs" style="left:191px;top:126px"><span>SKILL #1</span><span>40%</span></div>
  <div class="track abs" style="left:191px;top:133px"><div class="fill" style="width:48%"></div></div>
  <div class="skill-label abs" style="left:191px;top:146px"><span>SKILL #2</span><span>67%</span></div>
  <div class="track abs" style="left:191px;top:154px"><div class="fill" style="width:65%"></div></div>
</section>

<!-- Stats with graphic -->
<section class="slide" style="left:419px;top:349px">
  <div class="graphic-area abs" style="left:28px;top:35px;width:160px;height:133px" role="img" aria-label="Infographic of a downward and an upward arrow showing decrease and growth"></div>
  <div class="stat abs" style="left:51px;top:80px;width:38px;height:24px">
    <div class="stat__value">-157</div><div class="stat__label">Subtitle text</div>
  </div>
  <div class="stat abs" style="left:129px;top:97px;width:38px;height:24px">
    <div class="stat__value">+2,101</div><div class="stat__label">Subtitle text</div>
  </div>
  <h2 class="heading abs" style="left:213px;top:50px;font-size:15px">Title text slide</h2>
  <p class="copy abs" style="left:213px;top:71px;width:112px">Lorem ipsum dolor sit amet, consectetur adipisg elit, sed do eiusmod tempor incididunt ut labore et dolore magna aliqua. Ut enim ad minim vem, quis nostrud exercitation ullamco laboris nisi ut aliquip ex ea commo consequat. Duis aute irure dolor in reprehenderit in voluptate in velit esse cillum dolore eu fugiat nulla pariatur. Excepteur sint occaecat cupidatat non proident, sunt in culpa qui officia deserunt qui mollit anim id est natus error sit voluptatem accusantium doloue</p>
</section>

<!-- Text slide -->
<section class="slide" style="left:802px;top:349px">
  <h2 class="heading abs" style="left:36px;top:31px;font-size:15px">Title text slide</h2>
  <svg class="abs" style="left:36px;top:57px" width="30" height="10" aria-hidden="true">
    <line x1="4" y1="5" x2="26" y2="5" stroke="var(--accent)" stroke-width="1"/>
    <circle cx="3" cy="5" r="2" fill="var(--accent)"/>
    <circle cx="14" cy="5" r="4.5" fill="var(--accent)"/>
    <circle cx="25" cy="5" r="2" fill="var(--accent)"/>
  </svg>
  <p class="copy abs" style="left:36px;top:75px;width:284px">Lorem ipsum dolor sit amet, consectetur adipiscing elit, sed do eiusmod tempor incididunt ut labore et dolore magna aliqua. Ut enim ad minim veniam, quis nostrud exercitation ullamco laboris nisi ut aliquip ex ea commodo consequat. Duis aute irure dolor in reprehenderit in voluptate velit esse cillum dolore eu fugiat nulla pariatur. Excepteur sint occaecat cupidatat non proident, sunt in culpa qui officia deserunt mollit anim id est laborum.</p>
  <p class="copy abs" style="left:36px;top:107px;width:284px">Sed ut perspiciatis unde omnis iste natus error sit voluptatem accusantium doloremque laudantium, totam rem aperiam, voluptatem quia voluptas sit aspernatur aut odit aut fugit, sed quia consequuntur magni dolores eos qui ratione voluptatem sequi nesciunt. Neque porro quisquam est, qui dolorem ipsum quia dolor sit amet, consectetur, adipisci velit, sed quia non numquam eius modi tempora incidunt ut labore et dolore magnam vitae aliquam quaerat voluptatem. Ut enim ad minima veniam, quis nostrum exercitationem ullam corporis suscipit laboriosam, nisi ut aliquid ex ea commodi consequatur? Quis autem vel eum iure reprehenderit qui in ea voluptate velit esse quam nihil molestiae consequatur, vel illum qui dolorem eum fugiat quo voluptas nulla pariatur?</p>
</section>

</body>
</html>
```